Hardware Brand Packaging Design Project

We require a design for packaging for products in the retail hardware range. Initially this will be for a set of header cards for abrasive sanding discs but we plan to add other items to the range so we are looking for a range of brand elements that can be extended to other types of packaging.
The brand name is "Gleam Ridge" and we are looking for a black or dark grey background with a subtle fine pattern to break up the solid colour. This part of the design needs to be 'expandable' so that it can be used on different pack sizes as we increase the range. Two highlight or complimentary colours will add a bit of impact and become part of the brand style.
For printing purposes we have allowed for 4 colour process plus two spot colours and we have attached one of the header card dielines as a guide.
Target Market(s)
Home owners of both gender in the 25 to 55 age range
Industry/Entity Type
Printing
Requirements
Must have
- *The brand name "Gleam Ridge" should appear in the top left hand corner and we had in mind that the word would be a shiny metal / chrome appearance in could be in the shape of a shield or spear point but are open to any other suggestions.The word can be on one line or one above the other.
*Between the bottom of the hanger hole and the edge of the card is the words ABRASIVES & ACCESSORIES
*We want a performance guarantee device circle / seal or other in the bottom left quartile of the front facing panel. Circle device on attachment shows approx position.
* The right hand 25mm of the card is to be devoted to specific information about the product in the pack. This will be done by an adhered over-sticker ( see attached die-line No 2 )
* 3 line address panel or rear of card - QRT Abrasives, 47 Lane, West Auckland, New Zealand.
* Also somewhere on rear panel "Cut, Quality Checked & Packed in New Zealand from imported materials."
Nice to have
- It would be good, but not essential, to see a rough mock-up of how this design would transfer across to a box approx 80mm across the front, 100mm deep and 250mm high.

```html
<!DOCTYPE html>
<html lang="en">
<head>
<meta charset="utf-8">
<title>Gleam Ridge – Header Card</title>
<link href="https://fonts.googleapis.com/css2?family=Oswald:wght@500;700&family=Arimo:wght@400;700&display=swap" rel="stylesheet">
<style>
  :root {
    --paper: #ffffff;
    --card-dark: #141414;
    --card-mid: #3a3a3a;
    --card-light: #8a8a8a;
    --dieline: #111111;
    --accent-gold: #f5a623;
    --hole-edge: #1f2a7a;
    --hole-fill: #ffffff;
  }
  html, body {
    margin: 0;
    padding: 0;
    width: 1179px;
    height: 1200px;
    overflow: hidden;
    background: var(--paper);
  }
  .header-card {
    display: block;
    width: 1179px;
    height: 1200px;
  }
  .brand-name {
    font-family: "Oswald", sans-serif;
    font-weight: 700;
    fill: var(--accent-gold);
  }
  .range-title {
    font-family: "Oswald", sans-serif;
    font-weight: 500;
    fill: var(--accent-gold);
  }
  .rear-address {
    font-family: "Arimo", sans-serif;
    font-weight: 700;
    fill: var(--accent-gold);
  }
  .rear-origin {
    font-family: "Arimo", sans-serif;
    font-weight: 400;
    fill: var(--accent-gold);
  }
</style>
</head>
<body>
<svg class="header-card" viewBox="0 0 900 916" xmlns="http://www.w3.org/2000/svg">
  <defs>
    <radialGradient id="card-glow" cx="0.5" cy="0.52" r="0.6">
      <stop offset="0" stop-color="var(--card-light)"/>
      <stop offset="0.35" stop-color="var(--card-mid)"/>
      <stop offset="1" stop-color="var(--card-dark)"/>
    </radialGradient>
  </defs>

  <!-- Card body with dieline -->
  <path class="card-body" role="img" aria-label="Dark faceted cube pattern background with a soft central highlight"
        d="M40,48 Q40,36 52,36 H178 L186,44 Q445,170 700,44 L708,36 H852 Q864,36 864,48 V760 Q864,772 852,772 H708 L700,764 Q445,575 186,764 L178,772 H52 Q40,772 40,760 Z"
        fill="url(#card-glow)" stroke="var(--dieline)" stroke-width="2"/>

  <!-- Rear panel text (printed inverted for fold) -->
  <g class="rear-panel" transform="rotate(180 190 190)">
    <text class="rear-address" x="97" y="140" font-size="21">47 Lane</text>
    <text class="rear-address" x="97" y="164" font-size="21">West Auckland</text>
    <text class="rear-address" x="97" y="188" font-size="21">New Zealand.</text>
    <text class="rear-origin" x="97" y="214" font-size="12.5">Cut, Quality Checked &amp; Packed</text>
    <text class="rear-origin" x="97" y="233" font-size="12.5">in New Zealand</text>
    <text class="rear-origin" x="97" y="252" font-size="12.5">from imported materials.</text>
  </g>

  <!-- Hanger hole die cut -->
  <path class="hanger-hole"
        d="M330,272 H515 A17,17 0 0 1 515,306 H495 Q480,340 465,318 Q445,300 430,330 Q415,355 395,330 Q380,310 360,318 L300,400 L360,482 Q380,492 395,470 Q415,445 430,470 Q445,500 465,482 Q480,462 495,494 H515 A18,18 0 0 1 515,530 H330 Q318,530 310,520 L240,415 Q222,400 240,385 L310,282 Q318,272 330,272 Z"
        fill="var(--hole-fill)" stroke="var(--hole-edge)" stroke-width="2"/>

  <!-- Range title -->
  <g class="range-title-block">
    <text class="range-title" x="333" y="616" font-size="40">&amp;</text>
    <text class="range-title" x="378" y="585" font-size="20">ABRASIVES</text>
    <text class="range-title" x="378" y="614" font-size="20">ACCESSORIES</text>
  </g>

  <!-- Brand name -->
  <g class="brand-lockup">
    <text class="brand-name" x="130" y="492" font-size="36" text-anchor="middle">GLEAM</text>
    <text class="brand-name" x="130" y="534" font-size="36" text-anchor="middle">RIDGE</text>
  </g>

  <!-- Performance guarantee seal -->
  <circle class="guarantee-seal" cx="125" cy="690" r="42" fill="var(--accent-gold)"/>
</svg>
</body>
</html>
```